Flyer Design Project for Sports Medicine Services

I am a sports medicine doctor specialising in the diagnosis and management of sport and exercise injuries for all ages and levels of activity - from elite to weekend jogger. I work under the Business name Clear Stride Athletic Care and do have a company logo. I am wanting a flier that I can send to family doctors, physiotherapists and sports clubs explaining who I am what I can offer and why they should send me patients.
- I have a Masters in Sports Medicine (MSportsMed), Diplomas in Obstetrics/Gynaecology (DRANZCOG) and also Paediatrics (DCH) and certificate in advanced clinical hypnosis
-accurate diagnosis and management plan with their regular physio to return the player / athlete to the field / court /gym as soon as safely possible
-hypnosis for sports performance eg anxiety control, confidence and mental rehearsal for individuals and teams
- because there are many possible therapists and therapy options, as a sports doctor I can work out who they need to see a physiotherapist, surgeon, massage therapist chiropractor or podiatrist to return them to activity or whether cortisone, PRP or autologous blood injections are needed
-can provide one point of contact for coaches and clubs for rehabilitation and return to sport advice.
- work with Karen Holloway ex Australian Athlete, a Performance Strategist (NRB listed resource person) and registered Psychologist for best mental preparation for individuals teams and coach development
- can organise rapid access to MRI, ultrasound and specialist appointments if needed
-I work at 3 practices KineVista 518 Belford St Belford 86129437 Monday Wednesday Friday; Harrowgate Sports Clinic, 143 Harrowgate Rd, Adelaide 85917264 Tuesday Coastal Hawks Sports Medicine Clinic, Velloran Park 8561 3097 Thursday.
-facebook site clearstrideathleticcare
Updates
Hi All, just to clarify.. My name is Peter Dunstan and I am the sports doctor. My wife is Karen Holloway and she is the psychologist. The flier should mainly be advertising my sports medicine services and a byline ( or at least not the first line in the title) about the Performance Strategy and Coach development.
Target Market(s)
family doctors (GPs), Sporting Clubs, Physiotherapists
Industry/Entity Type
Massage
Look and feel

```html
<!DOCTYPE html>
<html lang="en">
<head>
<meta charset="utf-8">
<title>Clear Stride Athletic Care – Flyer</title>
<link href="https://fonts.googleapis.com/css2?family=Open+Sans:wght@400;600;700&family=Roboto+Condensed:wght@700&display=swap" rel="stylesheet">
<style>
  :root{
    --bg:#ececec;
    --paper:#ffffff;
    --green:#a8cf38;
    --blue:#1b9ad6;
    --sky:#2aa9e0;
    --grey:#c9c9c9;
    --ink:#3c3c3c;
    --title:#555555;
  }
  *{box-sizing:border-box;margin:0;padding:0}
  html,body{width:1200px;height:906px;overflow:hidden}
  body{background:var(--bg);font-family:"Open Sans",Arial,sans-serif;color:var(--ink);position:relative}

  .page{position:absolute;width:512px;height:724px;background:var(--paper);overflow:hidden;box-shadow:0 2px 8px rgba(0,0,0,.18)}
  .page--back{left:73px;top:100px}
  .page--front{left:611px;top:100px}

  /* plain straight colour bands */
  .band{position:absolute;left:0;width:512px}
  .band--green{background:var(--green)}
  .band--blue{background:var(--blue)}
  .band--grey{background:var(--grey)}

  /* back page */
  .web-address{position:absolute;right:18px;top:18px;font-size:9px;color:#222}
  .intro{position:absolute;left:27px;top:114px;width:300px;font-size:9.6px;line-height:15px;color:#222}
  .services{position:absolute;left:27px;top:172px;width:275px;list-style:none}
  .services li{position:relative;padding-left:20px;font-size:7.6px;line-height:10.3px;margin-bottom:7px}
  .services li::before{content:"";position:absolute;left:0;top:2px;width:9px;height:9px;border-radius:50%;background:var(--blue)}
  .about{position:absolute;left:27px;top:409px;width:230px;font-size:7.6px;line-height:11px}
  .about p{margin-bottom:8px}
  .about strong{font-weight:700}
  .contact{position:absolute;left:27px;top:544px;width:230px;font-size:7.6px;line-height:10.5px}
  .contact h3{font-size:7.6px;font-weight:400;margin-bottom:5px}
  .footnote{position:absolute;left:27px;top:599px;width:230px;font-size:6.8px;line-height:9.5px}

  .brand{position:absolute;text-align:center;color:var(--blue);font-weight:700;letter-spacing:-.3px}
  .brand__dot{display:block;margin:0 auto 8px;border-radius:50%;background:var(--green)}
  .page--back .brand{left:320px;top:120px;width:170px;font-size:16px;line-height:18px}
  .page--back .brand__dot{width:44px;height:44px}

  .urgent{position:absolute;left:320px;top:247px;width:170px;text-align:center;font-size:12.5px;line-height:15px;color:#222}
  .urgent .call{display:block;margin-top:4px;font-size:11px}
  .urgent .call b{font-size:18px;font-weight:700;margin-left:4px}
  .practices{position:absolute;left:330px;top:328px;width:150px;text-align:center;font-size:7px;line-height:12.6px;font-weight:600;color:#333}

  .photo{position:absolute}
  .photo--team{left:278px;top:457px;width:218px;height:218px;background:linear-gradient(160deg,#4e4a5a,#8a6f9a 45%,#d68a3c 80%,#3b3b48)}

  /* front page */
  .photo--match{left:0;top:0;width:512px;height:300px;background:linear-gradient(180deg,#7c9a5a 0%,#6f8a4a 35%,#c2453f 60%,#6b7f4a 100%)}
  .page--front .brand{left:160px;top:355px;width:192px;font-size:19px;line-height:21px}
  .page--front .brand__dot{width:56px;height:56px}
  .headline{position:absolute;left:0;top:525px;width:512px;text-align:center;font-family:"Roboto Condensed","Arial Narrow",sans-serif;font-weight:700;font-size:17.5px;line-height:27px;color:var(--title)}
  .gallery{position:absolute;left:0;top:595px;width:512px;height:129px;background:var(--sky)}
  .gallery .photo{top:5px;width:146px;height:112px;border:2px solid #fff;border-radius:9px}
  .photo--doctor{left:25px;background:linear-gradient(135deg,#5a8a3a,#8aa26a 55%,#e8e2da)}
  .photo--clinic{left:184px;background:linear-gradient(160deg,#d9d3c2,#b49a7c 55%,#5a4a44)}
  .photo--coaches{left:343px;background:linear-gradient(160deg,#7a6a5a,#e0c070 45%,#4a6aa0)}
</style>
</head>
<body>

<section class="page page--back" aria-label="Flyer back page">
  <div class="band band--green" style="top:0;height:36px"></div>
  <div class="band band--blue" style="top:40px;height:6px"></div>
  <div class="band band--grey" style="top:50px;height:4px"></div>
  <p class="web-address" style="color:#222">www.clearstrideathleticcare.com</p>

  <p class="intro">I have a Masters in Sports Medicine (MSportsMed), Diplomas in Obstetrics/Gynaecology (DRANZCOG) and also Paediatrics (DCH) and certificate in advanced clinical hypnosis.</p>

  <ul class="services">
    <li>accurate diagnosis and management plan with their regular physio to return the player / athlete to the field / court /gym as soon as safely possible</li>
    <li>hypnosis for sports performance eg anxiety control, confidence and mental rehearsal for individuals and teams</li>
    <li>because there are many possible therapists and therapy options, as a sports doctor I can work out who they need to see a physiotherapist, surgeon, massage therapist chiropractor or podiatrist to return them to activity or whether cortisone, PRP or autologous blood injections are needed</li>
    <li>can provide one point of contact for coaches and clubs for rehabilitation and return to sport advice.</li>
    <li>work with Karen Holloway ex Australian Athlete, a Performance Strategist (NRB listed resource person) and registered Psychologist for best mental preparation for individuals teams and coach development</li>
    <li>can organise rapid access to MRI, ultrasound and specialist appointments if needed</li>
  </ul>

  <div class="about">
    <p>Clear Stride Athletic Care aims to bring to you the best of high performance psychology whether it be for the sports field or practical concepts to bring to your business. Sports medicine services include diagnosis and management of all sport and exercise injuries with the aim to get you back to the sports field, court or gym in the quickest and safest manner.</p>
    <p><strong>Clear Stride Athletic Care provides profiling and consulting services from individuals to businesses regarding leadership, maximising individual performance, and improving coaches communication skills.</strong></p>
  </div>

  <div class="contact">
    <h3>Contacted on</h3>
    <p>M&nbsp;: 0412583906</p>
    <p>E&nbsp;: 9kholloway@netpost.com</p>
    <p>E&nbsp;: peterdunstan@clearstrideathleticcare.com</p>
  </div>
  <p class="footnote">Clear Stride Athletic Care is a Sports and Organisational Psychology and Sports Medicine service in Adelaide, South Australia brought to you by Karen Holloway and Dr Peter Dunstan.</p>

  <div class="brand"><span class="brand__dot"></span>Clear Stride<br>Athletic Care</div>

  <p class="urgent">URGENT SPORTS<br>INJURY ADVICE...<span class="call">Call<b>86129437</b></span></p>
  <p class="practices">3 practices KineVista 518 Belford St Belford 86129437 Monday Wednesday Friday; Harrowgate Sports Clinic, 143 Harrowgate Rd, Adelaide 85917264 Tuesday Coastal Hawks Sports Medicine Clinic, Velloran Park 8561 3097 Thursday.</p>

  <div class="photo photo--team" role="img" aria-label="Photo of a women's team in bright coloured shirts posing together indoors"></div>

  <div class="band band--grey" style="top:684px;height:4px"></div>
  <div class="band band--blue" style="top:692px;height:6px"></div>
  <div class="band band--green" style="top:702px;height:22px"></div>
</section>

<section class="page page--front" aria-label="Flyer front page">
  <div class="photo photo--match" role="img" aria-label="Photo of a women's lacrosse team in red uniforms huddled on a grass field"></div>
  <div class="band band--green" style="top:300px;height:8px"></div>
  <div class="band band--blue" style="top:311px;height:5px"></div>
  <div class="band band--grey" style="top:319px;height:3px"></div>

  <div class="brand"><span class="brand__dot"></span>Clear Stride<br>Athletic Care</div>

  <h1 class="headline">Dr. Peter Dunstan Sports Injuries Diagnosis and Treatment<br>Karen Holloway Sport Psychology and Leadership Programs</h1>

  <div class="gallery">
    <div class="photo photo--doctor" role="img" aria-label="Portrait photo of the sports doctor outdoors among greenery"></div>
    <div class="photo photo--clinic" role="img" aria-label="Photo of a group session in a clubroom"></div>
    <div class="photo photo--coaches" role="img" aria-label="Photo of four women from the coaching and performance team"></div>
  </div>
</section>

</body>
</html>
```